New look and feel for investment website

Hi

Our website needs a crisp and professional look and feel applying to it. Here’s the address: http://www.brightplinth.co.uk. Since posting the brief yesterday (Tuesday, 16 August), we've reduced the amount of content on the home page, which should make life a little easier for you. We will come back later today, with some points of reference in terms of sites we like the look of. (See below)

17 August, 1.20pm GMT. OK, comments generally on the designs submitted so far. Please keep in mind that images of graphs, piles of coins, paper money and pretty females are not what is required. Better to think in terms of abstract imagery instead. Ratios? Circles? Relationships? Patterns? Not money,sex,graphs etc. Hope that helps.

For guidance on look and feel, please refer to these sites, which we like:

http://www.morvelle.co.uk/
http://www.qz.com/
https://www.harrowfieldtamsin.com
https://www.pirelconcerns.com
https://www.kvantule.com
Updates

Here's the Tall Beacons logo created in AI CS5.

Our market is professional financial advisers and relatively sophisticated private investors. The look and feel therefore should be slick and sophisticated - not 'lively' and lightweight, more like a banking site. Please read the brief again where we've added a list of websites that we really like the look of to get a better feel for what we're looking for. Thanks once again, we appreciate the work you're putting in.

It's essential that all the elements that are on the current home page be included on all new designs. 

We use a device in our e-mails which you may wish to incorporate in your design.

Target Market(s)

Professional financial advisers. People who know about investment and money.

Industry/Entity Type

Investment

Requirements
Should not have
• Graphs or people.

```html
<!DOCTYPE html>
<html lang="en">
<head>
<meta charset="utf-8">
<title>Tall Beacons — Home</title>
<link href="https://fonts.googleapis.com/css2?family=Arimo:wght@400;700&family=PT+Sans&display=swap" rel="stylesheet">
<style>
  :root {
    --ink: #3a3a3a;
    --grey: #8a8a8a;
    --logo-grey: #7b7b7b;
    --light-grey: #a6a6a6;
    --rule: #d9d9d9;
    --accent: #f5a623;
    --red: #e5252a;
    --paper: #ffffff;
  }
  * { box-sizing: border-box; margin: 0; padding: 0; }
  html, body { width: 1200px; height: 1055px; overflow: hidden; background: var(--paper); }
  body { position: relative; font-family: "Arimo", Arial, sans-serif; color: var(--ink); }

  .utility-links {
    position: absolute; top: 114px; right: 202px;
    font-family: "PT Sans", sans-serif; font-size: 11px; color: var(--light-grey);
    display: flex; gap: 6px;
  }

  .brand { position: absolute; top: 160px; left: 190px; }
  .brand-name {
    font-family: "Arimo", sans-serif; font-weight: 400; font-size: 56px;
    letter-spacing: -1px; color: var(--logo-grey); line-height: 1;
  }

  .main-nav {
    position: absolute; top: 249px; left: 190px; width: 813px;
    display: flex; justify-content: space-between;
    font-size: 12.5px; color: var(--grey); text-transform: uppercase;
  }
  .main-nav .sep { color: var(--red); }
  .main-nav .sep.soft { color: var(--grey); }

  .hero {
    position: absolute; top: 277px; left: 189px; width: 815px; height: 197px;
    background: linear-gradient(180deg, #b9bdae 0%, #c6c9ab 45%, #a8ab8c 75%, #7c7f70 100%);
  }

  .feature-list { position: absolute; left: 190px; top: 510px; width: 268px; }
  .feature {
    position: absolute; left: 0; width: 268px; height: 85px;
    border: 1px solid var(--rule); display: flex;
  }
  .feature-thumb { width: 85px; height: 83px; flex: none; }
  .feature-body { padding: 8px 10px 0 11px; position: relative; flex: 1; }
  .feature-title { font-size: 14px; font-weight: 400; color: var(--accent); text-transform: uppercase; line-height: 17px; }
  .feature-text { font-size: 14.4px; line-height: 17.5px; color: var(--ink); }
  .feature-more { position: absolute; right: 12px; bottom: 4px; font-size: 8px; color: var(--light-grey); }

  .thumb-swirl { background: radial-gradient(circle at 50% 50%, #1a1a1a 0%, #6a6a6a 40%, #b8b8b8 100%); }
  .thumb-blur { background: linear-gradient(135deg, #4a4a4a 0%, #cfcfcf 40%, #5a5a5a 70%, #2e2e2e 100%); }
  .thumb-grid { background: linear-gradient(135deg, #c3cdd6 0%, #a9b7c3 100%); }

  .welcome { position: absolute; left: 494px; top: 503px; width: 512px; }
  .welcome h1 { font-weight: 400; font-size: 23px; color: var(--accent); margin-bottom: 10px; }
  .welcome h1 b { font-weight: 700; }
  .welcome p {
    font-size: 13.8px; line-height: 18.7px; text-align: justify; margin-bottom: 18.7px;
    letter-spacing: -0.1px; hyphens: auto; -webkit-hyphens: auto;
  }

  .footer-rule { position: absolute; left: 190px; top: 968px; width: 814px; height: 3px; background: var(--red); }
</style>
</head>
<body>
  <nav class="utility-links">
    <span>Login</span><span>|</span>
    <span>Register for free</span><span>|</span>
    <span>Contact us</span><span>|</span>
    <span>Terms &amp; Conditions</span>
  </nav>

  <header class="brand">
    <span class="brand-name">Tall Beacons</span>
  </header>

  <nav class="main-nav">
    <span>Home</span><span class="sep">|</span>
    <span>Two Minute Guide</span><span class="sep soft">|</span>
    <span>Performance</span><span class="sep">|</span>
    <span>Watch List</span><span class="sep soft">|</span>
    <span>Key Numbers</span><span class="sep">|</span>
    <span>Tested Results</span><span class="sep">|</span>
    <span>Trade History</span>
  </nav>

  <div class="hero" role="img" aria-label="Close-up of a circuit board with traced lines and soldered pads in pale grey-green tones"></div>

  <section class="feature-list">
    <article class="feature" style="top:0">
      <div class="feature-thumb thumb-swirl" role="img" aria-label="Abstract dark radial swirl"></div>
      <div class="feature-body">
        <h2 class="feature-title">FAQ’s</h2>
        <p class="feature-text">dolor sit amet,luctus al at cosectetuer adipiscin</p>
        <span class="feature-more">&gt;&gt; more</span>
      </div>
    </article>
    <article class="feature" style="top:111px">
      <div class="feature-thumb thumb-blur" role="img" aria-label="Abstract blurred light streaks in grey"></div>
      <div class="feature-body">
        <h2 class="feature-title">About our analysis</h2>
        <p class="feature-text">dolor sit amet,luctus al at cosectetuer adipiscin</p>
        <span class="feature-more">&gt;&gt; more</span>
      </div>
    </article>
    <article class="feature" style="top:225px">
      <div class="feature-thumb thumb-grid" role="img" aria-label="Soft blue-grey abstract texture"></div>
      <div class="feature-body">
        <h2 class="feature-title">Value investing</h2>
        <p class="feature-text">dolor sit amet,luctus al at cosectetuer adipiscin</p>
        <span class="feature-more">&gt;&gt; more</span>
      </div>
    </article>
    <article class="feature" style="top:337px">
      <div class="feature-thumb thumb-blur" role="img" aria-label="Abstract blurred light streaks in grey"></div>
      <div class="feature-body">
        <h2 class="feature-title">Halden 1000 / QX 500</h2>
        <p class="feature-text">dolor sit amet,luctus al at cosectetuer adipiscin</p>
        <span class="feature-more">&gt;&gt; more</span>
      </div>
    </article>
  </section>

  <main class="welcome">
    <h1>Welcome to <b>TALL</b>BEACONS.</h1>
    <p><b>Lorem ipsum</b> dolor sit amet, consectetuer adipiscing elit. Etiam nisi. Suspendisse luctus, nulla non feugiat ultrices, sem magna vulputate nunc, quis volutpat nunc nulla a mauris. Nunc non nisl id mi accumsan malesuada. In hac habitasse</p>
    <p>platea dictumst. Cum sociis natoque penatibus et magnis dis parturient montes, nascetur ridiculus mus. Ut et metus. Nunc nibh odio, varius eget, imperdiet sed, sagittis quis,</p>
    <p>metus. Nullam sagittis condimentum risus. Aenean nonummy, tortor a tempor scelerisque, tellus lorem elementum arcu, eget feugiat leo nisi et dolor. Aenean nonummy. Aliquam dui tortor, consectetuer eget, hendrerit eu, ornare quis, turpis. Donec venenatis, leo eu mattis adipiscing, est lacus pharetra lectus, sit amet faucibus pede ante adipiscing libero.</p>
    <p>Curabitur pretium. Proin pharetra nisi eget nisl. Aenean id nibh ac massa feugiat euismod. Donec venenatis ipsum ut massa. Donec dui massa, mattis eu, placerat vitae, aliquet nec, lacus. Aliquam urna odio, porttitor eu, ullamcor&shy;per a, ullamcor&shy;per nec, erat. Cras porta pretium orci. Lorem ipsum dolor sit amet, consectetuer adipiscing elit. Aliquam non elit ut nibh eleifend condimentum. Sed rhoncus lobor&shy;tis mauris. Proin volutpat ultrices diam. Maecenas sed libero. Maecenas fringilla</p>
  </main>

  <div class="footer-rule"></div>
</body>
</html>
```